Business Card for Voltrix

Horizontal business card for voltrix, the electrical contractor.
clean and professional looking, using company branding and colours.
I also want the blue in the logo and wording to be made a more 'electric' blue and the grey 'Voltrix' to be slightly darker.

Pleas use the following contact details:

Peter Alwick
Owner

t: 01632 960581
m: 07700 900316
e: peter@voltrix-wiring.co.uk

www.voltrix-wiring.co.uk

Industry/Entity Type

Electrical

Font styles to use
Sans Serif

```html
<!DOCTYPE html>
<html lang="en">
<head>
<meta charset="utf-8">
<title>Voltrix — Business Card</title>
<link rel="stylesheet" href="https://fonts.googleapis.com/css2?family=Questrial&display=swap">
<style>
  :root {
    --page-bg: #e9e9eb;
    --card-white: #ffffff;
    --card-dark: #1d1f23;
    --card-dark-edge: #2a2d33;
    --electric-blue: #1a5cff;
    --brand-grey: #3e4147;
    --text-grey: #4a4d52;
    --faint-grey: #e4e5e7;
    --faint-dark: #33363c;
  }
  * { box-sizing: border-box; margin: 0; padding: 0; }
  html, body {
    width: 1200px; height: 784px; overflow: hidden;
    background: var(--page-bg);
    font-family: "Questrial", "Century Gothic", sans-serif;
  }
  .sheet {
    position: relative; width: 1200px; height: 784px;
    display: flex; align-items: center; justify-content: center; gap: 40px;
  }
  .card {
    position: relative; width: 560px; height: 320px; overflow: hidden;
    border-radius: 4px;
    box-shadow: 0 8px 24px rgba(0,0,0,0.18);
  }

  /* Front */
  .card-front { background: var(--card-white); }
  .front-decor {
    position: absolute; right: -40px; top: 40px;
    width: 230px; height: 230px; border-radius: 50%;
    border: 26px solid var(--faint-grey);
  }
  .brand {
    position: absolute; left: 30px; top: 34px;
    display: flex; align-items: center; gap: 14px;
  }
  .brand-dot {
    width: 54px; height: 54px; border-radius: 50%;
    background: var(--electric-blue);
  }
  .brand-name {
    font-size: 56px; line-height: 1; letter-spacing: 10px;
    text-transform: uppercase; color: var(--brand-grey);
  }
  .brand-tagline {
    position: absolute; left: 98px; top: 96px;
    font-size: 19px; letter-spacing: 1.5px; text-transform: uppercase;
    color: var(--electric-blue);
  }
  .person { position: absolute; left: 30px; top: 150px; }
  .person-name { font-size: 22px; color: var(--electric-blue); font-weight: 700; }
  .person-role { font-size: 14px; color: var(--text-grey); margin-top: 4px; }
  .contacts {
    position: absolute; left: 30px; top: 206px;
    list-style: none; font-size: 17px; color: var(--text-grey);
  }
  .contacts li { display: flex; align-items: center; gap: 8px; height: 22px; }
  .contacts svg { width: 16px; height: 16px; fill: var(--electric-blue); flex: none; }
  .front-band {
    position: absolute; left: 0; right: 0; bottom: 0; height: 30px;
    background: linear-gradient(180deg, var(--card-dark-edge), var(--card-dark));
    border-top: 3px solid var(--electric-blue);
  }

  /* Back */
  .card-back {
    background: radial-gradient(ellipse at 50% 45%, var(--card-dark-edge), var(--card-dark) 75%);
  }
  .back-decor {
    position: absolute; left: 50%; top: 50%;
    width: 250px; height: 250px; margin: -125px 0 0 -125px;
    border-radius: 50%; border: 30px solid var(--faint-dark);
  }
  .back-url {
    position: absolute; left: 0; right: 0; top: 50%;
    transform: translateY(-50%); text-align: center;
    font-size: 20px; letter-spacing: 5px; color: var(--electric-blue);
  }
</style>
</head>
<body>
<main class="sheet">
  <section class="card card-front" aria-label="Business card front">
    <div class="front-decor" aria-hidden="true"></div>
    <div class="brand">
      <span class="brand-dot" aria-hidden="true"></span>
      <span class="brand-name">Voltrix</span>
    </div>
    <p class="brand-tagline">The Electrical Contractor</p>
    <div class="person">
      <p class="person-name">Peter Alwick</p>
      <p class="person-role">Owner</p>
    </div>
    <ul class="contacts">
      <li>
        <svg viewBox="0 0 16 16" aria-hidden="true"><path d="M3.6 1.5l2.3 2.6-1.2 1.8c.9 2 2.6 3.6 4.6 4.5l1.8-1.2 2.6 2.3-1.4 2.1C7 13.4 2.6 9 1.4 3L3.6 1.5z"/></svg>
        01632 960581
      </li>
      <li>
        <svg viewBox="0 0 16 16" aria-hidden="true"><path d="M4.5 1h7a1 1 0 0 1 1 1v12a1 1 0 0 1-1 1h-7a1 1 0 0 1-1-1V2a1 1 0 0 1 1-1zm.8 2v6h5.4V3H5.3zm1 7.5v1.2h1.2v-1.2H6.3zm2.2 0v1.2h1.2v-1.2H8.5zm-2.2 2v1.2h1.2v-1.2H6.3zm2.2 0v1.2h1.2v-1.2H8.5z"/></svg>
        07700 900316
      </li>
      <li>
        <svg viewBox="0 0 16 16" aria-hidden="true"><path d="M1 4h14v9H1V4zm1.4 1.2L8 9.2l5.6-4H2.4z"/></svg>
        peter@voltrix-wiring.co.uk
      </li>
    </ul>
    <div class="front-band" aria-hidden="true"></div>
  </section>

  <section class="card card-back" aria-label="Business card back">
    <div class="back-decor" aria-hidden="true"></div>
    <p class="back-url">www.voltrix-wiring.co.uk</p>
  </section>
</main>
</body>
</html>
```